Personalised Poetry business needs a business card designed

I am a writer that specialises in personalised poetry for people for significant life events.
I want a business card that stands out and portrays class and professionalism but is also welcoming & indicates warmth and honesty.
I'm happy with the logo that was designed for me, I would like to see it in raised print on the business card. I am open to suggestions on colours but think perhaps gold or silver writing for the logo would look good. I would like just the logo and my name and contact details on the front of the card. On the back of the card, I would like a list of the different events I provide poems for I will upload a photo of my current business card for reference. My current logo has a shading behind it that I don't like, I just want the words of the logo without any background colour

Target Market(s)

People wanting to provide a unique gift to someone special in their life

Industry/Entity Type

Writer

Contact Information for Business Card

Logo, my name and contact details on the front and a list of all the events I write poetry for on the back

Font styles to use
Script

Requirements
Must have
• I would like to see the logo, if possible, in a raised type of print on the card so that you can feel the actual words. I would like to have a glossy finish to the card and be able to print it on good quality board
Should not have
• The shading that is currently behind the logo on my current business card

```html
<!DOCTYPE html>
<html lang="en">
<head>
<meta charset="utf-8">
<title>Lines for Always – Business Card</title>
<link rel="stylesheet" href="https://fonts.googleapis.com/css2?family=Poppins:wght@300;400;600&family=Great+Vibes&display=swap">
<style>
  :root{
    --stage:#232323;
    --card-light:#ffffff;
    --card-dark:#343434;
    --band:#333333;
    --ink-dark:#2b2b2b;
    --ink-light:#f4f4f4;
    --ink-muted:#cfcfcf;
    --art-tone:#4a4a4a;
  }
  *{box-sizing:border-box;margin:0;padding:0}
  html,body{width:1200px;height:780px;overflow:hidden}
  body{background:var(--stage);font-family:'Poppins',sans-serif;display:flex;align-items:center;justify-content:center;gap:40px}
  .card{width:540px;height:310px;position:relative;overflow:hidden;box-shadow:0 10px 30px rgba(0,0,0,.5)}

  /* Front */
  .card--front{background:var(--card-light);color:var(--ink-dark)}
  .brand{position:absolute;text-align:center}
  .card--front .brand{top:34px;right:50px;width:300px}
  .brand__name{font-weight:400;font-size:32px;letter-spacing:.5px;line-height:1.1}
  .brand__tagline{font-weight:300;font-size:13px;letter-spacing:.5px;margin-top:4px}
  .band{position:absolute;left:0;right:0;top:156px;height:88px;background:var(--band);color:var(--ink-light);display:flex;align-items:center;padding:0 26px}
  .person{width:170px}
  .person__name{font-size:24px;line-height:1.05}
  .person__first{font-weight:600}
  .person__last{font-weight:300}
  .person__role{font-weight:300;font-size:12px;letter-spacing:.5px;margin-top:3px}
  .band__art{width:74px;height:74px;border-radius:6px;background:var(--art-tone);margin:0 20px 0 6px}
  .contact{list-style:none;font-size:12px;font-weight:300;display:flex;flex-direction:column;gap:8px}
  .contact li{display:flex;align-items:center;gap:8px}
  .contact svg{width:13px;height:13px;flex:none}
  .web{position:absolute;top:262px;left:0;right:0;display:flex;justify-content:center;align-items:center;gap:8px;font-size:13px;font-weight:300}
  .web svg{width:14px;height:14px}

  /* Back */
  .card--back{background:var(--card-dark);color:var(--ink-light)}
  .card--back .brand{top:30px;left:110px;width:330px}
  .card--back .brand__tagline{color:var(--ink-muted)}
  .services{position:absolute;top:130px;left:0;right:0;text-align:center}
  .services__title{font-family:'Great Vibes',cursive;font-size:26px;margin-bottom:6px}
  .services__list{list-style:none;font-size:13.5px;font-weight:300;line-height:1.55}
  .services__list li::before{content:"";display:inline-block;width:6px;height:6px;border-radius:50%;background:var(--ink-light);margin-right:8px;vertical-align:middle}
</style>
</head>
<body>
  <section class="card card--front" aria-label="Front of card">
    <div class="brand">
      <div class="brand__name">Lines for Always</div>
      <div class="brand__tagline">Personalised Poetry</div>
    </div>
    <div class="band">
      <div class="person">
        <div class="person__name"><span class="person__first">Ellis</span> <span class="person__last">Marren</span></div>
        <div class="person__role">Writer &amp; Owner</div>
      </div>
      <div class="band__art" role="img" aria-label="Line illustration of a hand writing with a fountain pen"></div>
      <ul class="contact">
        <li>
          <svg viewBox="0 0 24 24" fill="currentColor" aria-hidden="true"><path d="M6.6 10.8a15.1 15.1 0 0 0 6.6 6.6l2.2-2.2c.3-.3.7-.4 1-.2 1.1.4 2.3.6 3.6.6.6 0 1 .4 1 1V20c0 .6-.4 1-1 1A17 17 0 0 1 3 4c0-.6.4-1 1-1h3.5c.6 0 1 .4 1 1 0 1.3.2 2.5.6 3.6.1.3 0 .7-.2 1z"/></svg>
          0400 318 552
        </li>
        <li>
          <svg viewBox="0 0 24 24" fill="none" stroke="currentColor" stroke-width="2" aria-hidden="true"><rect x="3" y="5" width="18" height="14" rx="1"/><path d="M3 6l9 7 9-7"/></svg>
          ellis@linesforalways.com
        </li>
      </ul>
    </div>
    <div class="web">
      <svg viewBox="0 0 24 24" fill="none" stroke="currentColor" stroke-width="1.8" aria-hidden="true"><circle cx="12" cy="12" r="9"/><path d="M3 12h18M12 3c3 3 3 15 0 18M12 3c-3 3-3 15 0 18"/></svg>
      www.linesforalways.com
    </div>
  </section>

  <section class="card card--back" aria-label="Back of card">
    <div class="brand">
      <div class="brand__name">Lines for Always</div>
      <div class="brand__tagline">Personalised Poetry</div>
    </div>
    <div class="services">
      <h2 class="services__title">Momentous Life Events Personalised in Poetry</h2>
      <ul class="services__list">
        <li>Valentines Day</li>
        <li>Funerals &amp; Eulogies</li>
        <li>Birthdays &amp; Christmas</li>
        <li>Weddings &amp; Anniversaries</li>
        <li>Retirements, Business &amp; Corporate Events</li>
      </ul>
    </div>
  </section>
</body>
</html>
```